KTL Stewardship Powerpoint project

Hello, I would like a highly professional powerpoint design that uses the new logo that we had designed for my consulting company. I have created a starting point in powerpoint but the successful designer must take it to a new level. i would like to see a professional image on the front page as well as our website address on a banner at the bottom (www.ktlstewardship.com.au). It is going to be the document we use for presentations that will introduce my company so it must be special!

Industry/Entity Type

It Company

Requirements
Nice to have
• Some sort of design in the front page - attached is company logo for your use.

```html
<!DOCTYPE html>
<html lang="en">
<head>
<meta charset="utf-8">
<title>KTL Stewardship – Presentation Templates</title>
<link href="https://fonts.googleapis.com/css2?family=Open+Sans:wght@300;400;600;700&display=swap" rel="stylesheet">
<style>
:root{
  --blue:#1a6fc2;
  --blue-deep:#1456a6;
  --blue-soft:#3d8ad6;
  --grey:#8f9296;
  --grey-light:#c9cbce;
  --ink:#4a4d52;
  --canvas:#e1e2e4;
  --white:#ffffff;
}
*{box-sizing:border-box;margin:0;padding:0}
html,body{width:1200px;height:900px;overflow:hidden;background:var(--canvas);font-family:"Open Sans",Arial,sans-serif;color:var(--ink)}
.deck{position:absolute;left:124px;top:30px;display:grid;grid-template-columns:repeat(3,288px);grid-template-rows:repeat(5,162px);gap:5px 6px}
.slide{position:relative;background:var(--white);overflow:hidden}
.head{position:absolute;left:13px;top:16px;border-left:1px solid var(--blue);padding-left:6px}
.head h2{font-size:7px;font-weight:300;color:var(--blue);letter-spacing:.1px;line-height:1.1}
.head p{font-size:3.4px;color:var(--grey);margin-top:2px}
.brand{position:absolute;right:9px;top:10px;font-size:6px;font-weight:700;color:var(--blue);display:flex;align-items:center;gap:2px}
.brand i{display:block;width:4px;height:4px;background:var(--blue)}
.foot{position:absolute;left:0;right:0;bottom:0;height:4px;background:var(--blue);font-size:2.2px;color:#cfe2f6;padding:.8px 4px}
.copy{font-size:3px;line-height:1.5;color:var(--ink);text-align:justify}
.photo{position:absolute}

/* cover */
.cover .title{position:absolute;left:25px;top:38px;border-left:1px solid var(--blue);padding-left:6px;font-size:6px;font-weight:300;color:var(--ink);line-height:1.2}
.cover .title span{color:var(--blue);font-size:7px}
.cover .photo{left:0;top:65px;width:288px;height:72px;background:linear-gradient(90deg,#2a7fd3,#79b8ee 45%,#c9e3f8 80%,#eef6fd)}
.cover .legal{position:absolute;left:20px;top:152px;font-size:2.2px;color:var(--grey)}
.cover .foot{height:3px}

/* contents */
.blue-slide{background:linear-gradient(135deg,#2a66c0,#1d4fa8)}
.toc-label{position:absolute;left:37px;top:42px;color:var(--white);font-size:3.5px}
.toc-label strong{display:block;font-weight:300;font-size:10px;border-bottom:1px solid var(--white);width:20px;padding-bottom:1px;white-space:nowrap}
.toc{position:absolute;left:140px;top:53px;list-style:none}
.toc li{position:relative;width:122px;height:11px;margin-bottom:4px;background:#c9cfd8;font-size:4px;color:var(--blue-deep);padding:2.5px 0 0 19px}
.toc li b{position:absolute;left:0;top:-.5px;width:12px;height:12px;border-radius:50%;background:var(--grey);border:1.5px solid #e4e7ea;color:var(--white);font-size:4px;font-weight:400;text-align:center;line-height:9px}

/* about us grid */
.mosaic{position:absolute;left:19px;top:52px;display:grid;grid-template-columns:42px 42px;grid-template-rows:26px 26px 26px}
.mosaic div{font-size:3.2px;color:var(--white);display:flex;align-items:center;justify-content:center}
.mosaic .tone{background:linear-gradient(135deg,#d8dde3,#9aa3ad)}
.mosaic .fill{background:var(--blue)}
.two-col{position:absolute;left:108px;top:53px;display:grid;grid-template-columns:80px 80px;gap:8px}

/* about us 2 */
.about2 .bluebox{position:absolute;left:0;top:53px;width:94px;height:52px;background:var(--blue);color:var(--white);font-size:3.1px;line-height:1.6;padding:16px 10px 0 18px}
.about2 .photo{left:94px;top:53px;width:194px;height:52px;background:linear-gradient(90deg,#e9ebee,#b9bec4 50%,#eceef0)}
.about2 .copy{position:absolute;left:93px;top:114px;width:180px}

/* vision */
.vision{background:var(--grey)}
.vision .photo{left:0;top:0;width:288px;height:88px;background:linear-gradient(135deg,#2c6bc4,#1a58b0)}
.vision h2{position:absolute;left:18px;top:14px;font-size:6.5px;font-weight:300;color:var(--white)}
.vm-icon{position:absolute;top:70px;width:32px;height:32px;border-radius:50%;border:2px solid var(--white);background:var(--blue);display:flex;align-items:center;justify-content:center}
.vm-text{position:absolute;top:110px;width:96px;text-align:center;font-size:4.1px;line-height:1.3;color:var(--white);font-weight:300}

/* chart text */
.chart-text{position:absolute;left:19px;top:52px;width:128px}
.chart-text .copy{margin-bottom:5px}
.legend{position:absolute;left:193px;top:101px;list-style:none}
.legend li{font-size:2.4px;color:var(--ink);margin-bottom:7px;padding-left:5px;position:relative;width:45px}
.legend li::before{content:"";position:absolute;left:0;top:.5px;width:2.5px;height:2.5px;background:var(--blue)}
.legend li.g::before{background:var(--grey)}
.legend li.d::before{background:var(--blue-deep)}

/* donuts */
.donuts{position:absolute;left:22px;top:47px;display:grid;grid-template-columns:repeat(3,84px);gap:0}
.donut{text-align:center}
.donut .copy{text-align:center;font-size:2.8px;margin-top:8px;padding:0 10px;color:var(--grey)}

/* table */
.invest{position:absolute;left:40px;top:46px;width:196px;border-collapse:collapse;font-size:3.3px}
.invest caption{background:var(--blue);color:var(--white);font-weight:700;font-size:4.6px;text-align:left;padding:1.5px 3px;caption-side:top}
.invest td{border:.4px solid #c6c9cd;padding:.8px 3px;height:7.6px;white-space:nowrap}
.invest td.num{text-align:right}
.invest tr.total td{font-weight:700;border:none;border-top:.6px solid #888}

/* team */
.team{position:absolute;left:20px;top:46px;display:grid;grid-template-columns:repeat(3,84px);gap:6px}
.member{text-align:center}
.avatar{width:34px;height:34px;border-radius:50%;margin:0 auto;border:2px solid var(--blue-soft);background:radial-gradient(circle at 50% 40%,#e4e7ea,#a8b0b8)}
.member h3{font-size:3.4px;font-weight:400;color:var(--blue);margin-top:5px}
.member em{display:block;font-size:2.6px;color:var(--grey)}
.member .copy{text-align:center;font-size:2.7px;margin-top:5px}

/* partners */
.partners{position:absolute;left:60px;top:47px;width:174px;height:95px;border:.6px solid #d8dadc;box-shadow:0 1px 2px rgba(0,0,0,.08);display:grid;grid-template-columns:repeat(4,1fr);grid-template-rows:repeat(3,1fr);padding:8px 10px;gap:8px 14px}
.partners span{display:block;background:#c9ccd0;border-radius:1px}
.partners span.b{background:#9eb8d6}
.partners span.r{background:#d9a8a8}
.partners span.sq{width:14px;margin:0 auto}

/* solutions */
.lead{position:absolute;left:30px;top:48px;width:228px;text-align:center;font-size:3px;font-style:italic;color:var(--ink);line-height:1.5}
.solutions{position:absolute;left:32px;top:69px;display:grid;grid-template-columns:repeat(3,69px);grid-template-rows:38px 38px;gap:3px 10px}
.sol{border:1px solid var(--blue);padding:2px 4px;color:var(--blue)}
.sol.on{background:var(--blue);color:var(--white)}
.sol h4{font-size:3.6px;font-weight:400;display:flex;align-items:center;gap:3px;margin-bottom:3px}
.sol p{font-size:2.7px;line-height:1.4;color:inherit;opacity:.9}

/* services */
.services{position:absolute;left:45px;top:52px;display:grid;grid-template-columns:repeat(3,60px);gap:10px}
.svc .ico{height:37px;background:var(--blue);display:flex;align-items:center;justify-content:center}
.svc.grey .ico{background:var(--grey)}
.svc .txt{height:53px;margin-top:2px;background:var(--grey);color:var(--white);font-size:2.8px;line-height:1.45;text-align:center;padding:9px 4px 0}

/* image text */
.imgtext .panel{position:absolute;left:0;top:0;width:124px;height:162px;background:var(--blue);padding:16px 13px;color:var(--white)}
.imgtext h2{font-size:6.5px;font-weight:300;margin-left:5px}
.imgtext .copy{color:var(--white);margin-top:50px;font-size:3.2px;padding-left:5px}
.imgtext .brand{left:18px;top:auto;bottom:6px;right:auto;color:var(--white)}
.imgtext .brand i{background:var(--white)}
.imgtext .photo{left:124px;top:0;width:164px;height:162px;background:linear-gradient(90deg,#f2f2f2,#b5b5b5 45%,#6e6e6e 70%,#cfcfcf)}

/* section */
.section .photo{inset:0;background:linear-gradient(135deg,#3a85d3,#2a6fc4 60%,#4a8fd8)}
.section .info{position:absolute;left:127px;top:62px;width:34px;height:34px;border-radius:50%;background:var(--white);display:flex;align-items:center;justify-content:center}
.section .rule{position:absolute;left:107px;top:102px;width:74px;height:.6px;background:rgba(255,255,255,.7)}
.section h2{position:absolute;left:0;right:0;top:109px;text-align:center;font-size:7px;font-weight:300;color:var(--white)}

/* thanks */
.thanks .brand{top:8px;right:17px;font-size:9px}
.thanks .title{position:absolute;left:26px;top:39px;border-left:1px solid var(--blue);padding-left:6px;font-size:5.5px;font-weight:300;line-height:1.2;color:var(--ink)}
.thanks .title span{color:var(--blue);font-size:7.5px}
.thanks .map{left:0;top:66px;width:288px;height:76px;background:linear-gradient(120deg,#e4e6e2,#d9dde0 40%,#a9c6e6 55%,#dfe2e4 75%)}
.contact{position:absolute;left:24px;top:144px;right:8px;display:flex;justify-content:space-between;font-size:3.3px;color:var(--grey)}
.contact span{display:flex;align-items:center;gap:3px}
.contact i{display:block;width:5px;height:5px;border-radius:50%;background:var(--blue)}
.thanks .foot{height:3px}
</style>
</head>
<body>
<main class="deck">

  <!-- 1 cover -->
  <section class="slide cover">
    <div class="brand"><i></i>KTL Stewardship</div>
    <div class="title">CORPORATE OVERVIEW<br><span>2015</span></div>
    <div class="photo" role="img" aria-label="Row of glossy blue spheres in perspective"></div>
    <p class="legal">© 2015 KTL Stewardship. All rights reserved. Contains confidential and proprietary information and may not be disclosed or reproduced without prior written consent.</p>
    <div class="foot"></div>
  </section>

  <!-- 2 contents -->
  <section class="slide blue-slide" role="img" aria-label="Blue toned photo of a hand writing on a document">
    <div class="toc-label">TABLE OF<strong>CONTENTS</strong></div>
    <ol class="toc">
      <li><b>1</b>LOREM IPSUM DOLOR SIT MET</li>
      <li><b>2</b>LOREM IPSUM DOLOR SIT MET</li>
      <li><b>3</b>LOREM IPSUM DOLOR SIT MET</li>
      <li><b>4</b>LOREM IPSUM DOLOR SIT MET</li>
      <li><b>5</b>LOREM IPSUM DOLOR SIT MET</li>
      <li><b>6</b>LOREM IPSUM DOLOR SIT MET</li>
    </ol>
  </section>

  <!-- 3 about us -->
  <section class="slide">
    <div class="head"><h2>ABOUT US</h2><p>SUB TITLE GOES HERE</p></div>
    <div class="brand"><i></i>KTL Stewardship</div>
    <div class="mosaic">
      <div class="tone" role="img" aria-label="Row of spheres with one red leader"></div><div class="fill">Lorem ipsum</div>
      <div class="fill">Lorem ipsum</div><div class="tone" role="img" aria-label="Business team standing together"></div>
      <div class="tone" role="img" aria-label="Team meeting around a table"></div><div class="fill">Lorem ipsum</div>
    </div>
    <div class="two-col">
      <p class="copy">Lorem ipsum dolor sit amet, consectetur adipisicing elit, sed do eiusmod tempor incididunt ut labore et dolore magna aliqua. Ut enim ad minim veniam, quis nostrud exercitation ullamco laboris nisi ut aliquip ex ea commodo consequat. Duis aute irure dolor in reprehenderit in voluptate velit esse cillum dolore eu fugiat nulla pariatur.</p>
      <p class="copy">Lorem ipsum dolor sit amet, consectetur adipisicing elit, sed do eiusmod tempor incididunt ut labore et dolore magna aliqua. Ut enim ad minim veniam, quis nostrud exercitation ullamco laboris nisi ut aliquip ex ea commodo consequat. Duis aute irure dolor in reprehenderit in voluptate velit esse cillum dolore eu fugiat nulla pariatur.</p>
    </div>
    <div class="foot">© 2015 KTL Stewardship All rights reserved</div>
  </section>

  <!-- 4 about us 2 -->
  <section class="slide about2">
    <div class="head"><h2>ABOUT US</h2><p>SUB TITLE GOES HERE</p></div>
    <div class="brand"><i></i>KTL Stewardship</div>
    <div class="bluebox">LOREM IPSUM DOLOR SIT MET CONSECTETUR ADIPISICING ELIT SED DO EIUSMOD TEMPOR INCIDIDUNT UT LABORE ET DOLORE MAGNA</div>
    <div class="photo" role="img" aria-label="Group of smiling business people in a row"></div>
    <p class="copy">Lorem ipsum dolor sit amet, consectetur adipisicing elit, sed do eiusmod tempor incididunt ut labore et dolore magna aliqua. Ut enim ad minim veniam, quis nostrud exercitation ullamco laboris nisi ut aliquip ex ea commodo consequat. Duis aute irure dolor in reprehenderit in voluptate velit esse cillum dolore eu fugiat nulla pariatur.</p>
    <div class="foot">© 2015 KTL Stewardship All rights reserved</div>
  </section>

  <!-- 5 vision & mission -->
  <section class="slide vision">
    <div class="photo" role="img" aria-label="Blue toned photo of a hand signing a contract"></div>
    <h2>VISION &amp; MISSION</h2>
    <div class="vm-icon" style="left:60px">
      <svg width="16" height="12" viewBox="0 0 16 12"><circle cx="4" cy="7" r="3.2" fill="none" stroke="#fff" stroke-width="1.6"/><circle cx="12" cy="7" r="3.2" fill="none" stroke="#fff" stroke-width="1.6"/><rect x="6" y="3" width="4" height="3" fill="#fff"/></svg>
    </div>
    <div class="vm-icon" style="left:196px">
      <svg width="16" height="14" viewBox="0 0 16 14"><path d="M2 11 A6.5 6.5 0 1 1 14 11" fill="none" stroke="#fff" stroke-width="1.6"/><line x1="8" y1="9" x2="11" y2="5" stroke="#fff" stroke-width="1.4"/><circle cx="8" cy="9" r="1.2" fill="#fff"/></svg>
    </div>
    <p class="vm-text" style="left:28px">To provide state of the art logistical and supply chain solutions to the defined needs of our customers using the best people, processes and systems in creating efficient and effective results.</p>
    <p class="vm-text" style="left:164px">To provide state of the art logistical and supply chain solutions to the defined needs of our customers using the best people, processes and systems in creating efficient and effective results.</p>
  </section>

  <!-- 6 bar chart -->
  <section class="slide">
    <div class="head"><h2>OUR CHART</h2><p>SUB TITLE GOES HERE</p></div>
    <div class="brand"><i></i>KTL Stewardship</div>
    <div class="chart-text">
      <p class="copy">Lorem ipsum dolor sit amet consectetur adipisicing elit, sed do eiusmod tempor incididunt ut labore et dolore magna aliqua. Ut enim ad minim veniam, quis nostrud exercitation ullamco laboris nisi ut aliquip ex ea commodo consequat. Duis aute irure dolor in reprehenderit in voluptate velit esse cillum dolore eu fugiat nulla pariatur.</p>
      <p class="copy">Lorem ipsum dolor sit amet consectetur adipisicing elit, sed do eiusmod tempor incididunt ut labore et dolore magna aliqua. Ut enim ad minim veniam, quis nostrud exercitation ullamco laboris nisi ut aliquip ex ea commodo consequat. Duis aute irure dolor in reprehenderit in voluptate velit esse cillum dolore.</p>
      <p class="copy">Lorem ipsum dolor sit amet excepteur sint occaecat cupidatat non proident, sunt in culpa qui officia deserunt mollit anim id est laborum.</p>
    </div>
    <svg style="position:absolute;left:176px;top:38px" width="80" height="52" viewBox="0 0 80 52">
      <rect x="5" y="19" width="4" height="26" fill="#1a6fc2"/><rect x="10" y="28" width="4" height="17" fill="#8f9296"/>
      <rect x="24" y="24" width="4" height="21" fill="#1a6fc2"/><rect x="29" y="15" width="4" height="30" fill="#8f9296"/>
      <rect x="43" y="12" width="4" height="33" fill="#1a6fc2"/><rect x="48" y="23" width="4" height="22" fill="#1456a6"/>
      <rect x="62" y="16" width="4" height="29" fill="#1456a6"/><rect x="67" y="10" width="4" height="35" fill="#1a6fc2"/>
      <rect x="28" y="11" width="6" height="3" fill="#c9cbce"/><rect x="47" y="8" width="6" height="3" fill="#1a6fc2"/><rect x="66" y="6" width="6" height="3" fill="#1a6fc2"/>
      <line x1="0" y1="45" x2="78" y2="45" stroke="#c9cbce" stroke-width=".5"/>
      <g font-size="2.6" fill="#4a4d52" font-family="Open Sans, sans-serif"><text x="5" y="50">2009</text><text x="24" y="50">2010</text><text x="43" y="50">2011</text><text x="62" y="50">2012</text></g>
    </svg>
    <ul class="legend">
      <li><b>LOREM IPSUM</b><br>Lorem ipsum dolor sit amet consectetur adipisicing elit sed do</li>
      <li class="g"><b>LOREM IPSUM</b><br>Lorem ipsum dolor sit amet consectetur adipisicing elit sed do</li>
      <li class="d"><b>LOREM IPSUM</b></li>
    </ul>
    <div class="foot">© 2015 KTL Stewardship All rights reserved</div>
  </section>

  <!-- 7 donut chart -->
  <section class="slide">
    <div class="head"><h2>OUR CHART</h2><p>SUB TITLE GOES HERE</p></div>
    <div class="brand"><i></i>KTL Stewardship</div>
    <div class="donuts">
      <div class="donut">
        <svg width="40" height="40" viewBox="0 0 40 40"><circle cx="20" cy="20" r="16" fill="none" stroke="#c9cbce" stroke-width="4"/><circle cx="20" cy="20" r="16" fill="none" stroke="#1a6fc2" stroke-width="4" stroke-dasharray="81.4 100.5" transform="rotate(-90 20 20)"/><text x="20" y="22.5" text-anchor="middle" font-size="7" font-weight="700" fill="#1a6fc2" font-family="Open Sans, sans-serif">81%</text></svg>
        <p class="copy">dolor sit amet, consectetur adipisicing elit, sed do eiusmod tempor incididunt ut labore et dolore magna aliqua. Ut enim ad minim veniam quis nostrud exercitation ullamco laboris nisi ut aliquip ex ea esse cillum dolore eu fugiat nulla pariatur.</p>
      </div>
      <div class="donut">
        <svg width="40" height="40" viewBox="0 0 40 40"><circle cx="20" cy="20" r="16" fill="none" stroke="#c9cbce" stroke-width="4"/><circle cx="20" cy="20" r="16" fill="none" stroke="#1a6fc2" stroke-width="4" stroke-dasharray="72.4 100.5" transform="rotate(-90 20 20)"/><text x="20" y="22.5" text-anchor="middle" font-size="7" font-weight="700" fill="#1a6fc2" font-family="Open Sans, sans-serif">72%</text></svg>
        <p class="copy">dolor sit amet, consectetur adipisicing elit, sed do eiusmod tempor incididunt ut labore et dolore magna aliqua. Ut enim ad minim veniam quis nostrud exercitation ullamco laboris nisi ut aliquip ex ea esse cillum dolore eu fugiat nulla pariatur.</p>
      </div>
      <div class="donut">
        <svg width="40" height="40" viewBox="0 0 40 40"><circle cx="20" cy="20" r="16" fill="none" stroke="#c9cbce" stroke-width="4"/><circle cx="20" cy="20" r="16" fill="none" stroke="#1456a6" stroke-width="4" stroke-dasharray="63.3 100.5" transform="rotate(-90 20 20)"/><text x="20" y="22.5" text-anchor="middle" font-size="7" font-weight="700" fill="#1a6fc2" font-family="Open Sans, sans-serif">63%</text></svg>
        <p class="copy">dolor sit amet, consectetur adipisicing elit, sed do eiusmod tempor incididunt ut labore et dolore magna aliqua. Ut enim ad minim veniam quis nostrud exercitation ullamco laboris nisi ut aliquip ex ea esse cillum dolore eu fugiat nulla pariatur.</p>
      </div>
    </div>
    <div class="foot">© 2015 KTL Stewardship All rights reserved</div>
  </section>

  <!-- 8 table -->
  <section class="slide">
    <div class="head"><h2>OUR CHART</h2><p>SUB TITLE GOES HERE</p></div>
    <div class="brand"><i></i>KTL Stewardship</div>
    <table class="invest">
      <caption>Growth &amp; Income Investments</caption>
      <tr><td>Calm Bay</td><td>Delia</td><td>IRA</td><td>$</td><td class="num">178,445.44</td></tr>
      <tr><td>Northline Asset Management</td><td>Trust</td><td>NQ</td><td>$</td><td class="num">211,914.52</td></tr>
      <tr><td>Steady Ridge Portfolio</td><td>Trust</td><td>NQ</td><td>$</td><td class="num">177,033.59</td></tr>
      <tr><td>Wellcare Trust Partners</td><td>Owen</td><td>IRA</td><td>$</td><td class="num">269,724.35</td></tr>
      <tr><td>Silver</td><td>Owen</td><td>IRA</td><td>$</td><td class="num">37,766.03</td></tr>
      <tr><td>Valemont</td><td>Owen</td><td>IRA</td><td>$</td><td class="num">47,664.15</td></tr>
      <tr><td>Valemont</td><td>Delia</td><td>IRA</td><td>$</td><td class="num">10,745.27</td></tr>
      <tr><td>Corvane</td><td>Owen</td><td>IRA</td><td>$</td><td class="num">77,123.47</td></tr>
      <tr><td>Apex Row Capital</td><td>Owen</td><td>IRA</td><td>$</td><td class="num">58,843.79</td></tr>
      <tr><td>Apex Row Capital</td><td>Delia</td><td>IRA</td><td>$</td><td class="num">80,263.22</td></tr>
      <tr class="total"><td>Total Growth &amp; Income Investments</td><td></td><td></td><td>$</td><td class="num">1,147,563.83</td></tr>
    </table>
    <div class="foot">© 2015 KTL Stewardship All rights reserved</div>
  </section>

  <!-- 9 team -->
  <section class="slide">
    <div class="head"><h2>OUR CHART</h2><p>SUB TITLE GOES HERE</p></div>
    <div class="brand"><i></i>KTL Stewardship</div>
    <div class="team">
      <div class="member"><div class="avatar" role="img" aria-label="Portrait of the president"></div><h3>JONAH REED</h3><em>President</em><p class="copy">dolor sit amet, consectetur adipisicing elit, sed do eiusmod tempor incididunt ut labore et dolore magna aliqua. Ut enim ad minim veniam, quis nostrud exercitation ullamco laboris nisi ut aliquip ex ea commodo consequat fugiat nulla pariatur.</p></div>
      <div class="member"><div class="avatar" role="img" aria-label="Portrait of the CEO and founder"></div><h3>MARINA COLE</h3><em>CEO / Founder</em><p class="copy">dolor sit amet, consectetur adipisicing elit, sed do eiusmod tempor incididunt ut labore et dolore magna aliqua. Ut enim ad minim veniam, quis nostrud exercitation ullamco laboris nisi ut aliquip ex ea commodo consequat fugiat nulla pariatur.</p></div>
      <div class="member"><div class="avatar" role="img" aria-label="Portrait of the vice president"></div><h3>NADIA FROST</h3><em>Vice President</em><p class="copy">dolor sit amet, consectetur adipisicing elit, sed do eiusmod tempor incididunt ut labore et dolore magna aliqua. Ut enim ad minim veniam, quis nostrud exercitation ullamco laboris nisi ut aliquip ex ea commodo consequat fugiat nulla pariatur.</p></div>
    </div>
    <div class="foot">© 2015 KTL Stewardship All rights reserved</div>
  </section>

  <!-- 10 partners -->
  <section class="slide">
    <div class="head"><h2>OUR PARTNER</h2><p>SUB TITLE GOES HERE</p></div>
    <div class="brand"><i></i>KTL Stewardship</div>
    <div class="partners" aria-label="Partner marks">
      <span class="r"></span><span></span><span class="b"></span><span class="sq"></span>
      <span class="b"></span><span></span><span class="r"></span><span class="r sq"></span>
      <span class="r"></span><span class="r"></span><span></span><span class="sq"></span>
    </div>
    <div class="foot">© 2015 KTL Stewardship All rights reserved</div>
  </section>

  <!-- 11 solutions -->
  <section class="slide">
    <div class="head"><h2>OUR SOLUTIONS</h2><p>SUB TITLE GOES HERE</p></div>
    <div class="brand"><i></i>KTL Stewardship</div>
    <p class="lead">dolor sit amet, consectetur adipisicing elit, sed do eiusmod tempor incididunt ut labore et dolore magna aliqua.<br>Ut enim ad minim veniam, quis nostrud exercitation ullamco laboris nisi ut a</p>
    <div class="solutions">
      <div class="sol on"><h4>◉ Lorem ipsum dolor</h4><p>Dolor sit amet, consectetur adipisicing elit, sed do eiusmod tempor incididunt ut labore et dolore magna aliqua.</p></div>
      <div class="sol"><h4>◔ Lorem ipsum dolor</h4><p>Dolor sit amet, consectetur adipisicing elit, sed do eiusmod tempor incididunt ut labore et dolore magna aliqua.</p></div>
      <div class="sol on"><h4>◆ Lorem ipsum dolor</h4><p>Dolor sit amet, consectetur adipisicing elit, sed do eiusmod tempor incididunt ut labore et dolore magna aliqua.</p></div>
      <div class="sol"><h4>◷ Lorem ipsum dolor</h4><p>Dolor sit amet, consectetur adipisicing elit, sed do eiusmod tempor incididunt ut labore et dolore magna aliqua.</p></div>
      <div class="sol on"><h4>✲ Lorem ipsum dolor</h4><p>Dolor sit amet, consectetur adipisicing elit, sed do eiusmod tempor incididunt ut labore et dolore magna aliqua.</p></div>
      <div class="sol"><h4>▥ Lorem ipsum dolor</h4><p>Dolor sit amet, consectetur adipisicing elit, sed do eiusmod tempor incididunt ut labore et dolore magna aliqua.</p></div>
    </div>
    <div class="foot">© 2015 KTL Stewardship All rights reserved</div>
  </section>

  <!-- 12 services -->
  <section class="slide">
    <div class="head"><h2>OUR SERVICES</h2><p>SUB TITLE GOES HERE</p></div>
    <div class="brand"><i></i>KTL Stewardship</div>
    <div class="services">
      <div class="svc"><div class="ico"><svg width="16" height="16" viewBox="0 0 16 16"><path d="M8 1 L15 8 L8 15 L1 8 Z" fill="#fff"/><path d="M6 8 L10 8 M8.5 6 L10.5 8 L8.5 10" stroke="#1a6fc2" stroke-width="1.2" fill="none"/></svg></div><p class="txt">Dolor sit amet, consectetur adipisicing elit, sed do eiusmod tempor incididunt ut labore et dolore magna aliqua.</p></div>
      <div class="svc grey"><div class="ico"><svg width="16" height="17" viewBox="0 0 16 17"><circle cx="8" cy="10" r="6" fill="none" stroke="#fff" stroke-width="1.6"/><rect x="6.5" y="1" width="3" height="2" fill="#fff"/><line x1="8" y1="10" x2="8" y2="6.5" stroke="#fff" stroke-width="1.4"/></svg></div><p class="txt">Dolor sit amet, consectetur adipisicing elit, sed do eiusmod tempor incididunt ut labore et dolore magna aliqua.</p></div>
      <div class="svc"><div class="ico"><svg width="16" height="14" viewBox="0 0 16 14"><rect x="2" y="8" width="3" height="6" fill="#fff"/><rect x="6.5" y="5" width="3" height="9" fill="#fff"/><rect x="11" y="2" width="3" height="12" fill="#fff"/></svg></div><p class="txt">Dolor sit amet, consectetur adipisicing elit, sed do eiusmod tempor incididunt ut labore et dolore magna aliqua.</p></div>
    </div>
    <div class="foot">© 2015 KTL Stewardship All rights reserved</div>
  </section>

  <!-- 13 image text -->
  <section class="slide imgtext">
    <div class="panel">
      <h2>IMAGE TEXT</h2>
      <p class="copy">Lorem ipsum dolor sit amet, consectetur adipisicing elit, sed do eiusmod tempor incididunt ut labore et dolore magna aliqua. Ut enim ad minim veniam, quis nostrud exercitation ullamco laboris nisi ut aliquip ex ea commodo consequat. Duis aute irure dolor in reprehenderit in voluptate velit esse cillum dolore eu fugiat nulla pariatur.</p>
    </div>
    <div class="brand"><i></i>KTL Stewardship</div>
    <div class="photo" role="img" aria-label="Black and white photo of a smiling business team"></div>
  </section>

  <!-- 14 section title -->
  <section class="slide section">
    <div class="photo" role="img" aria-label="Blue toned office scene"></div>
    <div class="info"><svg width="14" height="18" viewBox="0 0 14 18"><circle cx="8" cy="3" r="2" fill="#1a6fc2"/><path d="M5 7 H9 L7 15 H10 L9.5 17 H3 L3.5 15 H5 L6.5 9 H4.5 Z" fill="#1a6fc2"/></svg></div>
    <div class="rule"></div>
    <h2>SECTION TITLE</h2>
  </section>

  <!-- 15 thank you -->
  <section class="slide thanks">
    <div class="brand"><i></i>KTL Stewardship</div>
    <div class="title">THANK YOU<br><span>FOR YOUR TIME</span></div>
    <div class="photo map" role="img" aria-label="Street map with a location pin at the office"></div>
    <svg style="position:absolute;left:237px;top:90px" width="7" height="10" viewBox="0 0 7 10"><path d="M3.5 10 L0.6 5 A3.3 3.3 0 1 1 6.4 5 Z" fill="#d93a2f"/><circle cx="3.5" cy="3.5" r="1.2" fill="#fff"/></svg>
    <div class="contact">
      <span><i></i>120 Harbour Crest Way Ste 400</span>
      <span><i></i>support@ktlstewardship.com</span>
      <span><i></i>www.ktlstewardship.com.au</span>
    </div>
    <div class="foot"></div>
  </section>

</main>
</body>
</html>
```